PHVR (Harborview Stomach Wellness Collective of Ridgeford)

We need a business card design for a new medical group that specializes in Gastroenterology (digestive diseases). We need a double sided card that is professional yet modern.
The front would incorporate our logo, names, titles and contact info. In the back we would like a map to our office as well as a space to write a follow up appointment.
Our address is:
4172 E. Marlow Ave, Suite 118, Las Vegas, NV 89147
phone: (702) 555-0172
fax: (702) 555-0139
website: www.quillbrookclinic.example
Target Market(s)
Physicians and patients
Industry/Entity Type
Medical
Contact Information for Business Card
Name
Title
phone: (702) 555-0172
fax: (702) 555-0139

```html
<!DOCTYPE html>
<html lang="en">
<head>
<meta charset="utf-8">
<title>PHVR Business Card</title>
<link rel="stylesheet" href="https://fonts.googleapis.com/css2?family=Cinzel:wght@500;600&family=Open+Sans:wght@400;600;700&display=swap">
<style>
  :root {
    --navy: #1d4f8f;
    --navy-deep: #133a72;
    --blue-band: #1f5aa3;
    --grey-text: #6f6f6f;
    --grey-rule: #b9b9b9;
    --ink: #1a1a1a;
    --card: #ffffff;
    --backdrop: #e9e9e9;
    --map-tone: #eef1f5;
  }
  * { box-sizing: border-box; margin: 0; padding: 0; }
  html, body { width: 1200px; height: 1000px; overflow: hidden; }
  body { background: var(--backdrop); position: relative; font-family: "Open Sans", Arial, sans-serif; }

  .card {
    position: absolute; left: 265px; width: 667px; height: 397px;
    background: var(--card); border-radius: 22px; overflow: hidden;
    box-shadow: 0 3px 10px rgba(0,0,0,.18);
  }
  .card--front { top: 73px; }
  .card--back { top: 533px; }

  /* Front */
  .brand { position: absolute; display: flex; align-items: center; }
  .brand__name { font-family: "Cinzel", Georgia, serif; font-weight: 600; line-height: 1; }
  .brand__divider { width: 1px; align-self: stretch; }
  .brand__full { font-family: "Cinzel", Georgia, serif; font-weight: 500; text-transform: uppercase; }

  .card--front .brand { left: 104px; top: 64px; height: 90px; }
  .card--front .brand__name { font-size: 88px; color: var(--navy); letter-spacing: 1px; }
  .card--front .brand__divider { background: var(--grey-rule); margin: 0 16px 0 18px; }
  .card--front .brand__full { font-size: 16px; line-height: 20px; color: var(--grey-text); }

  .person { position: absolute; top: 218px; width: 100%; text-align: center; font-family: "Cinzel", Georgia, serif; color: var(--navy-deep); }
  .person__name { font-size: 25px; font-weight: 600; }
  .person__title { font-size: 19px; font-weight: 500; }

  .contact { position: absolute; top: 268px; width: 100%; text-align: center; color: var(--grey-text); font-size: 17px; line-height: 29px; }
  .contact__phones { display: flex; justify-content: center; gap: 18px; }
  .contact__item { display: inline-flex; align-items: center; gap: 5px; }
  .contact__item svg { width: 14px; height: 14px; fill: var(--navy); }
  .contact__web b { color: var(--navy); font-weight: 700; letter-spacing: .5px; }

  .band { position: absolute; left: 0; bottom: 0; width: 100%; height: 33px; background: linear-gradient(90deg, var(--navy-deep), var(--blue-band) 50%, var(--navy-deep)); }

  /* Back */
  .header-band { position: absolute; left: 0; top: 0; width: 100%; height: 108px; background: linear-gradient(90deg, var(--navy-deep), var(--blue-band) 45%, var(--navy-deep)); }
  .card--back .brand { left: 32px; top: 34px; height: 60px; }
  .card--back .brand__name { font-size: 58px; color: #ffffff; }
  .card--back .brand__divider { background: rgba(255,255,255,.7); margin: 0 10px 0 12px; }
  .card--back .brand__full { font-size: 11.5px; line-height: 13.5px; color: #ffffff; }

  .appointment { position: absolute; left: 33px; top: 148px; }
  .appointment__row { display: flex; align-items: flex-end; height: 55px; font-weight: 700; font-size: 16px; color: var(--navy); }
  .appointment__label { width: 49px; }
  .appointment__line { border-bottom: 2px solid var(--ink); height: 1px; margin-bottom: 5px; }
  .appointment__line--date { width: 250px; }
  .appointment__line--time { width: 175px; }
  .appointment__suffix { margin-left: 9px; }

  .map-frame { position: absolute; left: 369px; top: 30px; width: 263px; height: 334px; border: 6px solid var(--blue-band); background: var(--map-tone); }
</style>
</head>
<body>

<section class="card card--front">
  <div class="brand">
    <span class="brand__name">PHVR</span>
    <span class="brand__divider"></span>
    <span class="brand__full">Harborview Stomach<br>Wellness<br>Collective of<br>Ridgeford</span>
  </div>

  <p class="person"><span class="person__name">Dana Whitlock</span> <span class="person__title">/ Owner</span></p>

  <div class="contact">
    <p class="contact__phones">
      <span class="contact__item">
        <svg viewBox="0 0 24 24" aria-hidden="true"><path d="M6.6 10.8a15.1 15.1 0 0 0 6.6 6.6l2.2-2.2a1 1 0 0 1 1-.25 11.4 11.4 0 0 0 3.6.57 1 1 0 0 1 1 1V20a1 1 0 0 1-1 1A17 17 0 0 1 3 4a1 1 0 0 1 1-1h3.5a1 1 0 0 1 1 1c0 1.25.2 2.45.57 3.57a1 1 0 0 1-.25 1z"/></svg>
        (702) 555-0172
      </span>
      <span class="contact__item">
        <svg viewBox="0 0 24 24" aria-hidden="true"><path d="M6 2h12v6H6zM4 9h16a2 2 0 0 1 2 2v6h-4v5H6v-5H2v-6a2 2 0 0 1 2-2zm4 8v3h8v-3z"/></svg>
        (702) 555-0139
      </span>
    </p>
    <p class="contact__web">www.<b>quillbrookclinic</b>.example</p>
    <p class="contact__address">4172 E. Marlow Ave, Suite 118, Las Vegas, NV 89147</p>
  </div>

  <div class="band"></div>
</section>

<section class="card card--back">
  <div class="header-band"></div>
  <div class="brand">
    <span class="brand__name">PHVR</span>
    <span class="brand__divider"></span>
    <span class="brand__full">Harborview Stomach<br>Wellness<br>Collective of<br>Ridgeford</span>
  </div>

  <div class="appointment">
    <div class="appointment__row"><span class="appointment__label">Date</span><span class="appointment__line appointment__line--date"></span></div>
    <div class="appointment__row"><span class="appointment__label">Time</span><span class="appointment__line appointment__line--time"></span><span class="appointment__suffix">am/pm</span></div>
    <div class="appointment__row"><span class="appointment__label">Date</span><span class="appointment__line appointment__line--date"></span></div>
    <div class="appointment__row"><span class="appointment__label">Time</span><span class="appointment__line appointment__line--time"></span><span class="appointment__suffix">am/pm</span></div>
  </div>

  <div class="map-frame" role="img" aria-label="Street map showing the route to the office at 4172 E. Marlow Ave"></div>
</section>

</body>
</html>
```